Investment Company Business Card Design

We need a Business Card design for a new company based in Boston called "Olt Investment". We are cooperating with local real estate and construction companies. Our company is very actively and aggressively acquiring primarily residential investment properties either to buy and hold long term or for purposes or renovating and repositioning for re-sale in the market. In addition, we undertake some development projects and acquisitions as opportunities present themselves. the final design should contains information about “Olt" the river boat. we are tenacious, indomitable, and the business have a favorable wind throughout the voyage for all our investment.
sample Info. on Design:
Tem Hollis
CEO
508-xxx-xxxx
415 Marrow St. Suite 108, Boston, MA 02127
Please provide a template also, that we can edit the info later.
Reason: i just got new LOGO Design attached will be use in Business Card Design.
Construction

```html
<!DOCTYPE html>
<html lang="en">
<head>
<meta charset="utf-8">
<title>Olt Investment – Business Card</title>
<link href="https://fonts.googleapis.com/css2?family=Exo+2:wght@400;500;600&display=swap" rel="stylesheet">
<style>
  :root {
    --page-bg: #e9e7e3;
    --card-white: #ffffff;
    --card-shade: #ececec;
    --ink: #2b2b2b;
    --ink-soft: #4a4a4a;
    --gold: #d9b35c;
    --gold-light: #e7c97f;
    --silver: #b9b9b9;
    --silver-light: #dcdcdc;
  }
  * { margin: 0; padding: 0; box-sizing: border-box; }
  html, body { width: 1200px; height: 800px; overflow: hidden; }
  body {
    background: var(--page-bg);
    font-family: "Exo 2", sans-serif;
    color: var(--ink);
    position: relative;
  }
  .business-card {
    position: absolute;
    left: 75px; top: 100px;
    width: 1050px; height: 600px;
    background: radial-gradient(ellipse at 40% 30%, var(--card-white) 0%, var(--card-white) 45%, var(--card-shade) 100%);
    box-shadow: 0 12px 30px rgba(0,0,0,0.18);
    overflow: hidden;
  }
  .card-waves { position: absolute; inset: 0; width: 100%; height: 100%; }
  .holder { position: absolute; left: 80px; top: 100px; }
  .holder-name { font-size: 30px; font-weight: 500; letter-spacing: 0.5px; }
  .holder-role { font-size: 20px; font-weight: 400; color: var(--ink-soft); margin-top: 4px; }
  .contact-list {
    position: absolute; left: 80px; top: 268px;
    list-style: none; font-size: 16px; color: var(--ink-soft);
  }
  .contact-list li { display: flex; align-items: center; height: 26px; white-space: nowrap; }
  .contact-list svg { width: 16px; height: 16px; margin-right: 10px; fill: var(--ink); flex: none; }
  .contact-list .address { padding-left: 26px; }
  .brand {
    position: absolute; right: 95px; top: 140px;
    display: flex; align-items: center; gap: 14px;
  }
  .brand-mark { width: 42px; height: 42px; border-radius: 50%; background: var(--gold); }
  .brand-name { font-size: 36px; font-weight: 600; color: var(--gold); letter-spacing: 1px; }
</style>
</head>
<body>
  <div class="business-card">
    <svg class="card-waves" viewBox="0 0 1050 600" preserveAspectRatio="none" aria-hidden="true">
      <defs>
        <linearGradient id="goldBand" x1="0" y1="0" x2="1" y2="0">
          <stop offset="0" stop-color="#d9b35c"/>
          <stop offset="0.5" stop-color="#e7c97f"/>
          <stop offset="1" stop-color="#d9b35c"/>
        </linearGradient>
        <linearGradient id="silverBand" x1="0" y1="0" x2="1" y2="0">
          <stop offset="0" stop-color="#dcdcdc"/>
          <stop offset="1" stop-color="#b9b9b9"/>
        </linearGradient>
      </defs>
      <path d="M0,486 C320,470 700,410 1050,288 L1050,336 C700,440 320,488 0,496 Z" fill="url(#silverBand)"/>
      <path d="M0,500 C320,492 700,450 1050,345 L1050,600 L0,600 Z" fill="url(#goldBand)"/>
    </svg>

    <div class="holder">
      <p class="holder-name">Dale Frost-Carver</p>
      <p class="holder-role">consultant</p>
    </div>

    <div class="brand">
      <span class="brand-mark"></span>
      <span class="brand-name">Olt Investment</span>
    </div>

    <ul class="contact-list">
      <li><svg viewBox="0 0 24 24"><path d="M6.6 10.8a15 15 0 0 0 6.6 6.6l2.2-2.2c.3-.3.7-.4 1-.2 1.1.4 2.3.6 3.6.6.6 0 1 .4 1 1V20c0 .6-.4 1-1 1C10.6 21 3 13.4 3 4c0-.6.4-1 1-1h3.5c.6 0 1 .4 1 1 0 1.3.2 2.5.6 3.6.1.3 0 .7-.2 1z"/></svg>508-xxx-xxxx</li>
      <li><svg viewBox="0 0 24 24"><path d="M7 1h10a2 2 0 0 1 2 2v18a2 2 0 0 1-2 2H7a2 2 0 0 1-2-2V3a2 2 0 0 1 2-2zm0 3v14h10V4zm5 15.5a1 1 0 1 0 0 2 1 1 0 0 0 0-2z"/></svg>508-xxx-xxxx</li>
      <li><svg viewBox="0 0 24 24"><path d="M7 2h8l3 3v4h1a2 2 0 0 1 2 2v9a2 2 0 0 1-2 2H5a2 2 0 0 1-2-2v-9a2 2 0 0 1 2-2h2zm2 2v5h7V6h-2V4zm-2 9v2h2v-2zm4 0v2h2v-2zm4 0v2h2v-2zm-8 3v2h2v-2zm4 0v2h2v-2zm4 0v2h2v-2z"/></svg>508-xxx-xxxx</li>
      <li><svg viewBox="0 0 24 24"><path d="M2 5h20v14H2zm2 2v.5l8 5 8-5V7zm0 2.8V17h16V9.8l-8 5z"/></svg>d.frost@oltinvestment.com</li>
      <li><svg viewBox="0 0 24 24"><path d="M12 2a10 10 0 1 0 0 20 10 10 0 0 0 0-20zm6.9 6h-3a15 15 0 0 0-1.3-3.9A8 8 0 0 1 18.9 8zM12 4c.8 1.2 1.5 2.5 1.9 4h-3.8c.4-1.5 1.1-2.8 1.9-4zM4.3 14a8 8 0 0 1 0-4h3.4a16 16 0 0 0 0 4zm.8 2h3a15 15 0 0 0 1.3 3.9A8 8 0 0 1 5.1 16zm3-8h-3a8 8 0 0 1 4.3-3.9C8.8 5.3 8.4 6.6 8.1 8zM12 20c-.8-1.2-1.5-2.5-1.9-4h3.8c-.4 1.5-1.1 2.8-1.9 4zm2.3-6H9.7a14 14 0 0 1 0-4h4.6a14 14 0 0 1 0 4zm.3 5.9c.6-1.2 1-2.5 1.3-3.9h3a8 8 0 0 1-4.3 3.9zm1.7-5.9a16 16 0 0 0 0-4h3.4a8 8 0 0 1 0 4z"/></svg>www.oltinvestment.com</li>
      <li class="address">415 Marrow St. Suite 108, Boston</li>
    </ul>
  </div>
</body>
</html>
```